依頼詳細
現在使っているものを画像データで添付します。
事務所ロゴをフォトショップデータで添付します。

参考に、市販の表紙デザインにはこういったものがあります。(下記リンク)
https://www.kazane-dk.co.jp/store/products/list.php?category_id=23
https://tomoriworks.com/item/certificate/
http://mizuho-kanade.com/front_cover/
A4の紙を綴じるものなので、A3より一回り大きいA3ワイドのレザック紙に印刷しております。こちら302×430mmサイズです。

表紙には、お客様(権利者)の名前と
その下には不動産の表示が入ります。(案件ごとに印刷します)
そのため、こちらを手差し印刷できるよう、高さ5センチ程度の空白を空けておいていただきたいです。

サイズ:A3ワイド(302×430mm)
2つ折り、左開きです。半分に折った部分が表紙となります。

色、デザインの雰囲気等お任せいたします。
公的で固い重要書類をいれるものですが、そういったイメージにはあまり縛られずなるべくオリジナリティのあるものを使いたいと思います。
記載項目
不動産登記権利情報

司法書士ふじさわ事務所
希望イメージ
シンプル 複雑
単色 カラフル
暗い 明るい
日常 高級
遊び心 厳粛
未来的 伝統的
女性的 男性的
希望する色
設定なし
納品ファイル
• イラストレーター形式 (.ai)
補足説明
設定なし
【追記】桐のマークについて
現在使っている権利証表紙には、司法書士バッヂの意匠である五三桐花をいれておりますが、今回は特に使用の指定はしません。
桐のマークを入れる場合については、五三桐でお願いいたします(葉っぱが中央に5枚・左右に3枚ずつの家紋)

(参考)
http://senra-mokudo.com/kamon-c/cate0/kiri/kiri2.html
https://www.ezukan-store.jp/img344/225970_3130817.html
■ 選んだ理由

見た瞬間に目を惹くデザインだと思い、選ばせていただきました。

■ 提案者全員のお礼・コメント

たくさんのご提案をいただき大変嬉しく思っております。
皆様それぞれ、素敵なデザインを考えていただき本当にありがとうございます。

```html
<!DOCTYPE html>
<html lang="ja">
<head>
<meta charset="utf-8">
<title>不動産登記権利情報</title>
<link rel="stylesheet" href="https://fonts.googleapis.com/css2?family=Noto+Sans+JP:wght@300;400&display=swap">
<style>
  :root {
    --paper: #ffffff;
    --navy: #1d3557;
    --blue: #a6bddb;
    --blue-pale: #c8d6ea;
    --grey: #cfd0d3;
    --ink: #333a44;
    --ink-soft: #5d6673;
    --rule: #8a9099;
  }
  * { margin: 0; padding: 0; box-sizing: border-box; }
  html, body { width: 853px; height: 1200px; overflow: hidden; background: var(--paper); }
  .cover {
    position: relative;
    width: 853px;
    height: 1200px;
    background: var(--paper);
    font-family: "Noto Sans JP", sans-serif;
    color: var(--ink);
  }
  .band { position: absolute; left: 0; width: 853px; }
  .band--top {
    top: 0;
    height: 156px;
    background: linear-gradient(90deg, var(--navy) 0%, var(--blue) 22%, var(--blue-pale) 50%, var(--grey) 75%, var(--navy) 100%);
  }
  .band--bottom {
    bottom: 0;
    height: 192px;
    background: linear-gradient(90deg, var(--navy) 0%, var(--blue) 25%, var(--grey) 50%, var(--blue) 75%, var(--navy) 100%);
  }

  .cover__title {
    position: absolute;
    top: 250px;
    left: 0;
    width: 853px;
    padding-left: 0.42em;
    text-align: center;
    font-weight: 300;
    font-size: 48px;
    letter-spacing: 0.42em;
    color: var(--ink);
  }
  .entry-line {
    position: absolute;
    left: 156px;
    width: 541px;
    height: 0;
    border-top: 1.5px solid var(--rule);
  }
  .entry-line--holder { top: 534px; }
  .entry-line--property { top: 619px; }

  .office {
    position: absolute;
    top: 836px;
    left: 156px;
    display: flex;
    align-items: flex-start;
    gap: 12px;
  }
  .office__mark {
    width: 92px;
    height: 92px;
    margin-top: 22px;
    background: var(--blue-pale);
  }
  .office__text { display: flex; flex-direction: column; width: 450px; }
  .office__role {
    font-size: 30px;
    font-weight: 400;
    letter-spacing: 19px;
    color: var(--ink-soft);
    line-height: 1.45;
  }
  .office__name {
    font-size: 37px;
    font-weight: 400;
    letter-spacing: 25px;
    color: var(--ink);
    line-height: 1.3;
  }
  .office__address,
  .office__contact {
    font-size: 17px;
    font-weight: 400;
    letter-spacing: 0.16em;
    color: var(--ink-soft);
    line-height: 2.1;
  }
  .office__contact { display: flex; justify-content: space-between; width: 444px; }
</style>
</head>
<body>
<main class="cover">
  <div class="band band--top" role="img" aria-label="上部の幾何学模様の装飾帯"></div>

  <h1 class="cover__title">不動産登記権利情報</h1>

  <div class="entry-line entry-line--holder"></div>
  <div class="entry-line entry-line--property"></div>

  <section class="office">
    <div class="office__mark" aria-hidden="true"></div>
    <div class="office__text">
      <p class="office__role">司法書士・行政書士</p>
      <p class="office__name">ふじさわ事務所</p>
      <p class="office__address">〒071-0512 北海道空知郡中町3丁目12番地</p>
      <p class="office__contact"><span>TEL 0123-45-6780</span><span>FAX 0123-45-6781</span></p>
    </div>
  </section>

  <div class="band band--bottom" role="img" aria-label="下部の幾何学模様の装飾帯"></div>
</main>
</body>
</html>
```